Psychotherapist need a business card with logo

I am a psychotherapist in need of a business card. The card must have:

Moravia Telvundor
Psicoterapeuta
937 218 604

Psychologists use the greek letter psy, which is the psychologist symbol, but I would prefer something like a mandala, a graphic symbol, an iconic tree, nothing very usual, but something that shows confidence and trust.

Industry/Entity Type

Business

```html
<!DOCTYPE html>
<html lang="es">
<head>
<meta charset="utf-8">
<title>Moravia Telvundor · Psicoterapeuta</title>
<link href="https://fonts.googleapis.com/css2?family=Yellowtail&family=Josefin+Sans:wght@400&family=Raleway:wght@300&display=swap" rel="stylesheet">
<style>
  :root {
    --backdrop: #e9e6e1;
    --card-navy: #2f3aa6;
    --card-navy-light: #4453c4;
    --card-navy-deep: #27308f;
    --band-sky: #a7d6ee;
    --band-sky-light: #bfe3f4;
    --trim: #8fb9e2;
    --accent-lime: #d9ea5c;
    --ink-navy: #2d3a9e;
    --mark-white: #f4f6ff;
  }
  * { box-sizing: border-box; margin: 0; padding: 0; }
  html, body {
    width: 1200px;
    height: 902px;
    overflow: hidden;
    background: var(--backdrop);
  }
  .canvas {
    position: relative;
    width: 1200px;
    height: 902px;
  }
  .business-card {
    position: absolute;
    left: 365px;
    top: 51px;
    width: 470px;
    height: 800px;
    overflow: hidden;
    background: radial-gradient(ellipse at 55% 35%, var(--card-navy-light), var(--card-navy) 60%, var(--card-navy-deep));
    box-shadow: 0 14px 34px rgba(0, 0, 0, 0.28);
  }
  .logo-mark {
    position: absolute;
    left: 128px;
    top: 120px;
    width: 214px;
    height: 214px;
    border-radius: 50%;
    background: var(--mark-white);
  }
  .identity {
    position: absolute;
    left: 0;
    right: 0;
    top: 430px;
    text-align: center;
  }
  .identity__name {
    font-family: "Yellowtail", cursive;
    font-size: 46px;
    font-weight: 400;
    color: var(--accent-lime);
    line-height: 1;
  }
  .identity__role {
    margin-top: 8px;
    padding-left: 120px;
    font-family: "Josefin Sans", sans-serif;
    font-size: 21px;
    color: var(--accent-lime);
    letter-spacing: 0.5px;
  }
  .contact-band {
    position: absolute;
    left: 0;
    right: 0;
    top: 520px;
    height: 200px;
    background: linear-gradient(180deg, var(--band-sky-light), var(--band-sky));
  }
  .contact-band::after {
    content: "";
    position: absolute;
    left: 0;
    right: 0;
    bottom: -10px;
    height: 10px;
    background: var(--trim);
  }
  .contact-band__icon {
    position: absolute;
    left: 214px;
    top: 70px;
    width: 42px;
    height: 42px;
  }
  .contact-band__phone {
    position: absolute;
    left: 0;
    right: 0;
    top: 128px;
    text-align: center;
    font-family: "Raleway", sans-serif;
    font-weight: 300;
    font-size: 40px;
    letter-spacing: 1px;
    color: var(--ink-navy);
  }
</style>
</head>
<body>
<main class="canvas">
  <article class="business-card">
    <div class="logo-mark" role="img" aria-label="Round mandala logo mark in white"></div>

    <header class="identity">
      <h1 class="identity__name">Moravia Telvundor</h1>
      <p class="identity__role">Psicoterapeuta</p>
    </header>

    <section class="contact-band">
      <svg class="contact-band__icon" viewBox="0 0 42 42" aria-hidden="true">
        <circle cx="21" cy="21" r="21" fill="var(--ink-navy)"/>
        <rect x="15" y="10" width="12" height="22" rx="2" fill="none" stroke="var(--band-sky-light)" stroke-width="2"/>
        <circle cx="21" cy="28" r="1.4" fill="var(--band-sky-light)"/>
      </svg>
      <p class="contact-band__phone">937 218 604</p>
    </section>
  </article>
</main>
</body>
</html>
```